Webiste Design KLV

Design the website using uploaded content. Design colors should match that of the company logo with an allowance of one more extra color if it makes the website look much better and colorful. Use Technology related stock images in your design.

Target Market(s)

Potential Clients - Companies

Industry/Entity Type

Information Technology

Coding

Coded - Design and coding required

Number of Pages Required

5+ page

Requirements
Must have
• Company Logo Colors
Nice to have
• Professional Look and Feel with Sliders showing professional information technology images

```html
<!DOCTYPE html>
<html lang="en">
<head>
<meta charset="utf-8">
<title>KLV Technologies</title>
<link href="https://fonts.googleapis.com/css2?family=Poppins:wght@400;500;600;700;800&display=swap" rel="stylesheet">
<style>
:root{
  --blue:#1f45b5;
  --blue-deep:#122a7a;
  --navy:#0d1d55;
  --orange:#f7931e;
  --ink:#111522;
  --muted:#5a6072;
  --light:#f4f6fb;
  --white:#ffffff;
}
*{box-sizing:border-box;margin:0;padding:0}
html,body{width:1200px;height:4084px;overflow:hidden}
body{font-family:"Poppins",sans-serif;color:var(--ink);background:var(--white);position:relative}
.abs{position:absolute}
.btn{display:inline-flex;align-items:center;justify-content:center;background:var(--orange);color:var(--white);font-weight:600;font-size:17px;border-radius:4px;height:44px;padding:0 30px}
.btn-white{background:var(--white);color:var(--blue);font-size:15px;height:40px;border-radius:3px}
.section-title{font-size:40px;font-weight:700;text-align:center;color:var(--ink)}
.section-title span{color:var(--blue)}
.body-text{font-size:13px;line-height:1.75;color:var(--muted)}

/* hero */
.hero{left:0;top:0;width:1200px;height:600px;background:radial-gradient(ellipse at 30% 40%,#3b67dc 0%,rgba(59,103,220,0) 55%),radial-gradient(ellipse at 80% 70%,#2a4fc0 0%,rgba(42,79,192,0) 50%),linear-gradient(180deg,#2a56d0 0%,#1c3fae 60%,#1a3a9c 100%)}
.nav{left:0;top:0;width:1200px;height:60px;background:rgba(13,29,85,.35);display:flex;align-items:center;padding:0 40px}
.brand{color:var(--white);font-weight:800;font-size:22px;letter-spacing:1px;display:flex;align-items:center;gap:10px}
.brand i{width:16px;height:16px;background:var(--orange);display:block;border-radius:50%}
.nav ul{list-style:none;display:flex;gap:30px;margin-left:115px;color:var(--white);font-size:15px;font-weight:500}
.nav .quote{height:38px;font-size:15px;padding:0 20px}
.search{margin-left:auto;margin-right:20px}
.hero h1{left:0;width:1200px;text-align:center;color:var(--white);font-size:64px;font-weight:700;line-height:1.1}
.hero p{left:300px;width:600px;top:296px;text-align:center;color:var(--white);font-size:16px;line-height:1.5}
.partners{left:64px;top:452px;width:1072px;display:flex;gap:16px}
.partner{width:168px;height:124px;background:var(--white);display:flex;align-items:center;justify-content:center;font-weight:700;font-size:24px;color:var(--blue)}
.arrow{width:32px;height:32px;border-radius:50%;background:var(--white);display:flex;align-items:center;justify-content:center}

/* photo areas */
.photo{box-shadow:0 10px 28px rgba(13,29,85,.22)}
.photo-office{background:radial-gradient(circle at 35% 35%,#e9d9c8 0%,rgba(233,217,200,0) 40%),linear-gradient(135deg,#9aa9c8,#dfe5f0 55%,#7b8db4)}
.photo-team{background:radial-gradient(circle at 60% 45%,#c9a98f 0%,rgba(201,169,143,0) 38%),linear-gradient(135deg,#34497e,#7f93bd 60%,#c6cfe2)}
.photo-tablet{background:radial-gradient(circle at 50% 55%,#ffffff 0%,rgba(255,255,255,0) 45%),linear-gradient(160deg,#e6e9f0,#aeb9cf 60%,#6e7fa6)}
.photo-dark{background:radial-gradient(circle at 40% 45%,#8a6f5c 0%,rgba(138,111,92,0) 40%),linear-gradient(135deg,#1d2233,#4b566f 55%,#8b97ae)}
.photo-meeting{background:radial-gradient(circle at 55% 40%,#cdb39d 0%,rgba(205,179,157,0) 40%),linear-gradient(135deg,#3a4a72,#8392b3 55%,#d2d8e6)}
.mission-title{left:606px;top:730px;font-size:40px;font-weight:700}
.mission-title span,.vision-title span{color:var(--blue)}

/* governance */
.gov{left:0;top:1060px;width:1200px;height:500px;background:var(--light)}
.gov-card{top:1172px;width:344px;height:350px;color:var(--white);padding:0 18px}
.gov-card.g1{background:linear-gradient(180deg,rgba(31,69,181,0) 30%,rgba(31,69,181,.92) 75%),linear-gradient(135deg,#c8b8a6,#7f8fb2)}
.gov-card.g2{background:linear-gradient(180deg,rgba(31,69,181,0) 30%,rgba(31,69,181,.92) 75%),linear-gradient(135deg,#6d7fa8,#d4c2b1)}
.gov-card.g3{background:linear-gradient(180deg,rgba(31,69,181,0) 30%,rgba(31,69,181,.92) 75%),linear-gradient(135deg,#a7b3cc,#5c6d96)}
.gov-card h3{position:absolute;top:192px;font-size:22px;font-weight:700}
.gov-card p{position:absolute;top:226px;left:18px;right:40px;font-size:11px;line-height:1.45}
.gov-card .btn{position:absolute;top:296px;left:18px;height:34px;font-size:13px;padding:0 16px}

/* solutions */
.sol-icon{top:2128px;width:84px;height:84px;border-radius:50%;background:var(--orange);display:flex;align-items:center;justify-content:center;box-shadow:0 0 0 10px #fde3c3}
.sol-card{top:2272px;width:300px;height:226px;background:var(--white);box-shadow:0 6px 24px rgba(17,21,34,.1);text-align:center;padding:40px 24px}
.sol-card h3{font-size:18px;font-weight:600;margin-bottom:14px}
.sol-card p{font-size:11px;line-height:1.6;color:var(--muted)}

/* clients */
.clients{left:0;top:2980px;width:1200px;height:240px;background:linear-gradient(180deg,#1c3fae,#14307f)}
.client{width:140px;height:100px;background:var(--white);display:flex;align-items:center;justify-content:center;font-weight:700;font-size:16px;color:var(--navy)}

/* contact */
.field{left:588px;width:528px;height:52px;border:1px solid #b7bdca;border-radius:3px;font-size:14px;color:var(--muted);padding:16px 12px}

/* footer */
.footer{left:0;top:3828px;width:1200px;height:256px;background:linear-gradient(180deg,#1c3fae,#12287a);color:var(--white)}
.footer h4{font-size:26px;font-weight:700}
.footer .addr{font-size:14px;line-height:1.35}
.social{width:32px;height:32px;border-radius:50%;background:var(--white)}
</style>
</head>
<body>

<!-- Hero -->
<section class="hero abs">
  <nav class="nav abs">
    <div class="brand"><i></i>KLV</div>
    <ul><li>Home ▾</li><li>Company ▾</li><li>Services ▾</li><li>Portfolio ▾</li><li>Blog ▾</li><li>Elements ▾</li><li>Contact</li></ul>
    <svg class="search" width="18" height="18" viewBox="0 0 18 18"><circle cx="7.5" cy="7.5" r="6" stroke="#fff" stroke-width="2" fill="none"/><line x1="12" y1="12" x2="17" y2="17" stroke="#fff" stroke-width="2"/></svg>
    <span class="btn quote">Free Quote</span>
  </nav>
  <h1 class="abs" style="top:136px">Welcome To</h1>
  <h1 class="abs" style="top:208px">KLV Technologies</h1>
  <p class="abs">Our Company is built on the assumption that the management of information technology for business is like legal advice or accounting.</p>
  <span class="btn btn-white abs" style="left:528px;top:372px;padding:0 20px">→ Learn More</span>
  <div class="arrow abs" style="left:20px;top:498px"><svg width="12" height="12" viewBox="0 0 12 12"><path d="M8 1 3 6l5 5" stroke="#1f45b5" stroke-width="2" fill="none"/></svg></div>
  <div class="partners abs">
    <div class="partner">Vantix</div><div class="partner">Norvel</div><div class="partner">Qubra</div><div class="partner">Teklo</div><div class="partner">Ravion</div><div class="partner">Lumora</div>
  </div>
  <div class="arrow abs" style="left:1148px;top:498px"><svg width="12" height="12" viewBox="0 0 12 12"><path d="m4 1 5 5-5 5" stroke="#1f45b5" stroke-width="2" fill="none"/></svg></div>
</section>

<!-- Mission -->
<section>
  <div class="abs" style="left:140px;top:660px;width:300px;height:330px;border:2px solid var(--blue)"></div>
  <div class="photo photo-office abs" role="img" aria-label="Businesswoman smiling in a modern office" style="left:100px;top:690px;width:210px;height:230px"></div>
  <div class="photo photo-team abs" role="img" aria-label="Team meeting around a laptop" style="left:240px;top:800px;width:200px;height:200px"></div>
  <h2 class="mission-title abs">Mission <span>Statement</span></h2>
  <p class="body-text abs" style="left:606px;top:800px;width:520px">To provide end-to-end ICT as well as Engineering solutions and services that allow our customers to focus on achieving their business objectives. We will take care of your technology issues so that you can focus on running and growing your business. Our goal is to increase the productivity, efficiency and profits of your company by working in partnership with your company. It will assist you to be reliable, and useful technology environment.</p>
  <span class="btn abs" style="left:606px;top:940px;height:38px;font-size:14px;padding:0 22px">Read More</span>
</section>

<!-- Governance -->
<section class="gov abs"></section>
<h2 class="section-title abs" style="left:0;top:1100px;width:1200px">Governance, <span>Risk And Etchis</span></h2>
<article class="gov-card g1 abs" role="img" aria-label="Team collaborating at a desk" style="left:56px"><h3>Integrity</h3><p>We believe that all decisions are done with integrity. Every choice we make will put clients first.</p><span class="btn">→ Read More</span></article>
<article class="gov-card g2 abs" role="img" aria-label="Support agent with headset" style="left:428px"><h3>Customer Service</h3><p>We believe that customers are our first priority and we strive for great quality. We listen to clients and respond quickly.</p><span class="btn">→ Read More</span></article>
<article class="gov-card g3 abs" role="img" aria-label="Colleagues reviewing charts" style="left:800px"><h3>Continuous Improvement</h3><p>We believe that everyday we strive to be better at what we do, adapting to new ideas and methods with professional commitment.</p><span class="btn">→ Read More</span></article>

<!-- Vision -->
<section>
  <h2 class="vision-title abs" style="left:180px;top:1690px;font-size:40px;font-weight:700">Vision <span>Statement</span></h2>
  <p class="body-text abs" style="left:180px;top:1750px;width:420px">Our vision is to be the most innovative and preferred ICT and Engineering Company that becomes trusted to grow the business locally and internationally.</p>
  <span class="btn abs" style="left:466px;top:1816px;height:38px;font-size:14px;padding:0 22px">Read More</span>
  <div class="abs" style="left:720px;top:1620px;width:260px;height:330px;border:2px solid var(--blue)"></div>
  <div class="photo photo-tablet abs" role="img" aria-label="Hands using a tablet with digital graphics" style="left:688px;top:1650px;width:260px;height:300px"></div>
</section>

<!-- Solutions -->
<h2 class="section-title abs" style="left:0;top:2030px;width:1200px">Solutions and Service <span>Offerings</span></h2>
<div class="sol-icon abs" style="left:178px"><svg width="36" height="36" viewBox="0 0 36 36"><circle cx="18" cy="18" r="14" stroke="#fff" stroke-width="3" fill="none"/><path d="M11 18l5 5 9-10" stroke="#fff" stroke-width="3" fill="none"/></svg></div>
<div class="sol-icon abs" style="left:558px"><svg width="36" height="36" viewBox="0 0 36 36"><circle cx="18" cy="18" r="5" fill="#fff"/><g stroke="#fff" stroke-width="3"><line x1="18" y1="2" x2="18" y2="10"/><line x1="18" y1="26" x2="18" y2="34"/><line x1="2" y1="18" x2="10" y2="18"/><line x1="26" y1="18" x2="34" y2="18"/></g></svg></div>
<div class="sol-icon abs" style="left:912px"><svg width="36" height="36" viewBox="0 0 36 36"><path d="M9 5c2 0 4 6 4 7s-3 2-3 4 6 9 9 10c2 0 3-3 4-3s7 2 7 4-3 5-6 5C14 32 4 21 4 11c0-3 3-6 5-6z" fill="#fff"/></svg></div>
<article class="sol-card abs" style="left:70px"><h3>Infrastructure Solutions</h3><p>KLV Technologies has a strong team of skilled and dedicated engineers. Each office is fully staffed with certified professionals ready to support clients across the region.</p></article>
<article class="sol-card abs" style="left:450px"><h3>Converged Communication</h3><p>Converged Communication Systems provide one flexible platform for voice, data and video. Our unified solutions help teams connect with ease.</p></article>
<article class="sol-card abs" style="left:804px"><h3>Managed Print Services</h3><p>KLV Technologies partners with leading print brands to deliver reliable print management, lower costs and ensure devices always stay productive.</p></article>

<!-- Industries -->
<section>
  <div class="abs" style="left:120px;top:2560px;width:400px;height:360px;border:2px solid var(--blue)"></div>
  <div class="photo photo-dark abs" role="img" aria-label="Business team working together at laptops" style="left:100px;top:2590px;width:400px;height:320px"></div>
  <h2 class="abs" style="left:600px;top:2604px;font-size:40px;font-weight:700">Industries</h2>
  <p class="body-text abs" style="left:600px;top:2674px;width:520px;font-size:12px">Overview<br>Our Traffic Control System is a leading ICT system in the world. In our current urban traffic signal technology, traffic jams, data processing and system optimisation are our strengths. It can integrate urban traffic management and help people to reduce energy consumption and reduce traffic accidents.<br>The system can connect with police traffic controllers and other ICT systems. In addition, it provides software programming interface for developers.<br>The system can be used to build a whole urban management solution with proper transportation planning, traffic operation and control strategy.</p>
  <span class="btn abs" style="left:600px;top:2868px;height:38px;font-size:14px;padding:0 22px">Read More</span>
</section>

<!-- Clients -->
<section class="clients abs">
  <h2 class="abs" style="left:0;top:28px;width:1200px;text-align:center;color:#fff;font-size:40px;font-weight:700">Our Clints</h2>
  <div class="arrow abs" style="left:20px;top:134px"><svg width="12" height="12" viewBox="0 0 12 12"><path d="M8 1 3 6l5 5" stroke="#1f45b5" stroke-width="2" fill="none"/></svg></div>
  <div class="abs" style="left:78px;top:100px;display:flex;gap:12px">
    <div class="client">Marendo</div><div class="client">Ostrava</div><div class="client">Pellwin</div><div class="client">Corvane</div><div class="client">Zentari</div><div class="client">Halvero</div><div class="client">Brisken</div>
  </div>
  <div class="arrow abs" style="left:1148px;top:134px"><svg width="12" height="12" viewBox="0 0 12 12"><path d="m4 1 5 5-5 5" stroke="#1f45b5" stroke-width="2" fill="none"/></svg></div>
</section>

<!-- Contact -->
<section>
  <div class="abs" style="left:100px;top:3318px;width:440px;height:470px;border:2px solid var(--blue)"></div>
  <div class="photo photo-meeting abs" role="img" aria-label="Professionals meeting in a conference room" style="left:72px;top:3332px;width:440px;height:446px"></div>
  <h2 class="abs" style="left:588px;top:3340px;font-size:40px;font-weight:700">Contact Us</h2>
  <div class="field abs" style="top:3412px">Your Name</div>
  <div class="field abs" style="top:3480px">Enter your name</div>
  <div class="field abs" style="top:3548px;height:146px">Message</div>
  <span class="btn abs" style="left:588px;top:3716px;width:172px;height:52px;font-size:18px">Submit</span>
</section>

<!-- Footer -->
<footer class="footer abs">
  <div class="brand abs" style="left:74px;top:52px"><i></i>KLV</div>
  <p class="abs" style="left:74px;top:116px;font-size:14px">© 2023 KLV technologies</p>
  <div class="abs" style="left:74px;top:150px;display:flex;gap:10px"><span class="social"></span><span class="social"></span><span class="social"></span><span class="social"></span><span class="social"></span></div>
  <h4 class="abs" style="left:310px;top:40px">Address</h4>
  <p class="addr abs" style="left:310px;top:84px">14 Kestrel Lane<br>Rivermoor<br>0412<br>P. O. Box 2281<br>Elmsdale<br>0415</p>
  <p class="addr abs" style="left:516px;top:40px">Block 3<br>8 Harbour Crescent<br>Westfield<br>Northgate<br>2177<br>PO Box 519<br>Ashby<br>2179</p>
  <h4 class="abs" style="left:748px;top:40px">Join Our Newsletter</h4>
  <div class="abs" style="left:748px;top:96px;width:364px;height:46px;border:1px solid #fff;font-size:14px;padding:13px 14px">Enter your email</div>
  <div class="abs" style="left:748px;top:158px;width:364px;height:46px;background:#fff;color:var(--navy);font-weight:700;font-size:18px;display:flex;align-items:center;justify-content:center">Subscribe</div>
</footer>

</body>
</html>
```